Let Us Bloom speaking engagement

the flyer is about a speaking engagement for women's groups. Flyer should be simple, soft, engaging, clean and professional. I am a life coach and also a talk show host. the event I will be advertising is for groups of women. It will be given to church groups, female clubs and organizations. The name of my company is Mara's Lantern Life Coaching Institute.

Target Market(s)

professional women over thirty years old

Font styles to use
Script

Colors
ffffff
34a7d8
85cae6

Requirements
Must have
• use my photo and logo only
Should not have
• anything distracting

```html
<!DOCTYPE html>
<html lang="en">
<head>
<meta charset="utf-8">
<title>Let Us Bloom – A Heart to Heart Conversation</title>
<link rel="stylesheet" href="https://fonts.googleapis.com/css2?family=Poppins:wght@300;400;600&family=Allura&display=swap">
<style>
  :root {
    --white: #ffffff;
    --brand-blue: #34a7d8;
    --soft-blue: #85cae6;
    --teal: #3aa8bd;
    --text-grey: #585858;
    --photo-teal: #6fcfd6;
    --photo-light: #f4f7df;
    --photo-warm: #f6b3a0;
  }
  * { box-sizing: border-box; margin: 0; padding: 0; }
  html, body { width: 979px; height: 1200px; overflow: hidden; background: var(--white); }
  .flyer {
    position: relative;
    width: 979px;
    height: 1200px;
    background: var(--white);
    font-family: "Poppins", sans-serif;
    overflow: hidden;
  }
  .hero-photo {
    position: absolute;
    left: 0; top: 0;
    width: 979px; height: 560px;
    background:
      radial-gradient(ellipse 260px 200px at 520px 250px, rgba(246,179,160,0.55), transparent 70%),
      radial-gradient(ellipse 420px 300px at 700px 160px, var(--photo-light), transparent 75%),
      linear-gradient(120deg, var(--photo-teal) 0%, #a9e0e2 45%, var(--photo-light) 100%);
    -webkit-mask-image: linear-gradient(to bottom, #000 78%, transparent 100%);
    mask-image: linear-gradient(to bottom, #000 78%, transparent 100%);
  }
  .headline {
    position: absolute;
    top: 20px; left: 0; width: 100%;
    text-align: center;
    color: var(--brand-blue);
  }
  .headline__title {
    font-weight: 600;
    font-size: 54px;
    letter-spacing: 1px;
    line-height: 1.1;
  }
  .headline__subtitle {
    font-weight: 400;
    font-size: 31px;
    line-height: 1.2;
  }
  .event-name {
    position: absolute;
    top: 555px; left: 0; width: 100%;
    text-align: center;
  }
  .event-name__tell {
    font-weight: 300;
    font-size: 64px;
    letter-spacing: 3px;
    color: var(--teal);
    line-height: 1;
  }
  .event-name__to {
    font-weight: 300;
    font-size: 34px;
    color: var(--brand-blue);
    line-height: 1;
    margin-top: -2px;
  }
  .event-name__script {
    font-family: "Allura", cursive;
    font-size: 120px;
    color: var(--brand-blue);
    line-height: 0.8;
    margin-top: -4px;
  }
  .intro {
    position: absolute;
    top: 808px; left: 60px; width: 859px;
    text-align: center;
    font-weight: 300;
    font-size: 20px;
    line-height: 1.3;
    color: var(--text-grey);
  }
  .invite-box {
    position: absolute;
    top: 883px; left: 64px;
    width: 864px; height: 78px;
    border: 2px solid var(--brand-blue);
    text-align: center;
    font-weight: 300;
    font-size: 20px;
    line-height: 1.55;
    color: var(--text-grey);
    padding-top: 5px;
  }
  .institute-name {
    position: absolute;
    top: 992px; left: 230px; width: 540px;
    text-align: center;
    font-weight: 400;
    font-size: 24px;
    color: var(--brand-blue);
  }
  .footer-band {
    position: absolute;
    left: 0; top: 1067px;
    width: 979px; height: 133px;
    background: var(--brand-blue);
    text-align: center;
    color: var(--white);
    padding-left: 80px;
  }
  .footer-band__name {
    font-weight: 300;
    font-size: 27px;
    letter-spacing: 0.5px;
    margin-top: 18px;
  }
  .footer-band__contact {
    font-weight: 600;
    font-size: 23px;
    letter-spacing: 1px;
    margin-top: 6px;
  }
  .coach-portrait {
    position: absolute;
    left: 45px; top: 972px;
    width: 172px; height: 172px;
    border-radius: 50%;
    border: 5px solid #e6e6e6;
    background: radial-gradient(circle at 50% 45%, #7a5a48 0%, #3b2f2c 55%, #8fa39a 100%);
    z-index: 2;
  }
</style>
</head>
<body>
  <main class="flyer">
    <div class="hero-photo" role="img" aria-label="Photo of a joyful woman in a white dress with arms spread wide against a bright teal and sunlit sky"></div>

    <header class="headline">
      <h1 class="headline__title">A HEART TO HEART</h1>
      <p class="headline__subtitle">conversation with Life Coach Talia Brooks.</p>
    </header>

    <section class="event-name">
      <p class="event-name__tell">TELL IT</p>
      <p class="event-name__to">TO</p>
      <p class="event-name__script">Talia!</p>
    </section>

    <p class="intro">Let Us Bloom is an interactive soul searching session that will help women share their stories and be real about the things that matter most.</p>

    <div class="invite-box">
      <p>To invite Talia to your women's group or gathering.</p>
      <p>Contact us at 242-555-0148 or 555-0192</p>
    </div>

    <p class="institute-name">Mara's Lantern Life Coaching Institute</p>

    <div class="coach-portrait" role="img" aria-label="Portrait photo of Life Coach Talia Brooks"></div>

    <footer class="footer-band">
      <p class="footer-band__name">LIFE COACH TALIA BROOKS</p>
      <p class="footer-band__contact">Contact us at 242-555-0148 or 555-0192</p>
    </footer>
  </main>
</body>
</html>
```